Enterteinment new company in Costa Rica who wants to attract international artists

We need a business design for s new company from Costa Rica Called Velvet Harbor Shows. Our core business is Produce Alternative Rock Concerts. We would like to see a very creative business card connected to music ideas. Our logo is Black so we would like to see not too many colors on it. Silver letters would be great combined with black.

Target Market(s)

Entertainment

Industry/Entity Type

Entertainment

Contact Information for Business Card

We would like something different, creative.

Font styles to use
Other font styles liked:
• voltaire

Colors
000000
ffffff

Requirements
Must have
• We are looking for a creative business card
Nice to have
• liked to music

```html
<!DOCTYPE html>
<html lang="en">
<head>
<meta charset="utf-8">
<title>Velvet Harbor Shows – Business Card</title>
<link href="https://fonts.googleapis.com/css2?family=Voltaire&family=Ubuntu:wght@400;700&display=swap" rel="stylesheet">
<style>
  :root {
    --ink: #000000;
    --card: #0b0b0b;
    --silver: #ffffff;
    --silver-soft: #cfcfcf;
    --silver-dim: #8a8a8a;
    --splash: #3a3a3a;
    --bar: #5a5a5a;
    --backdrop: #e4e2de;
  }
  * { margin: 0; padding: 0; box-sizing: border-box; }
  html, body {
    width: 1200px; height: 900px; overflow: hidden;
    background: var(--backdrop);
  }
  .canvas { position: relative; width: 1200px; height: 900px; }

  .card {
    position: absolute;
    width: 560px; height: 320px;
    background: linear-gradient(160deg, #141414 0%, var(--card) 55%, var(--ink) 100%);
    border-radius: 4px;
    box-shadow: 0 10px 28px rgba(0,0,0,.35);
    overflow: hidden;
    color: var(--silver);
  }
  .card--front { left: 60px; top: 100px; }
  .card--back  { left: 580px; top: 480px; }

  /* front */
  .ink-splash {
    position: absolute; left: 150px; top: 70px; width: 250px; height: 180px;
    background: radial-gradient(ellipse at center, var(--splash) 0%, #262626 45%, rgba(20,20,20,0) 72%);
  }
  .brand-mark {
    position: absolute; right: 58px; top: 26px;
    display: flex; align-items: center; gap: 10px;
    font-family: "Voltaire", sans-serif; font-size: 24px; color: var(--silver);
    letter-spacing: .5px;
  }
  .brand-mark .dot { width: 14px; height: 14px; border-radius: 50%; background: var(--silver); }
  .person { position: absolute; left: 26px; top: 178px; }
  .person__name {
    font-family: "Ubuntu", sans-serif; font-weight: 700; font-size: 24px; color: var(--silver-soft);
  }
  .person__title {
    font-family: "Ubuntu", sans-serif; font-size: 14px; color: var(--silver-dim); margin-top: 2px;
  }
  .contact {
    position: absolute; left: 200px; bottom: 20px; list-style: none;
    font-family: "Ubuntu", sans-serif; font-size: 12.5px; color: var(--silver); line-height: 20px;
    white-space: nowrap;
  }
  .contact li { display: flex; align-items: center; gap: 8px; }
  .contact svg { width: 11px; height: 11px; fill: var(--silver); flex: none; }
  .website {
    position: absolute; font-family: "Ubuntu", sans-serif; font-size: 11px; color: var(--silver-soft);
    white-space: nowrap;
  }
  .card--front .website {
    right: 12px; top: 70px; writing-mode: vertical-rl;
  }

  /* back */
  .equalizer {
    position: absolute; left: 0; top: 0; width: 220px; height: 320px;
  }
  .equalizer rect { fill: var(--bar); }
  .tagline-block { position: absolute; left: 190px; top: 118px; }
  .tagline-block__name {
    font-family: "Voltaire", sans-serif; font-size: 40px; line-height: 1; color: var(--silver);
    letter-spacing: 1px; text-transform: uppercase; white-space: nowrap;
  }
  .tagline-block__line {
    font-family: "Voltaire", sans-serif; font-size: 13px; color: var(--silver-soft);
    letter-spacing: 1.2px; margin-top: 8px; text-transform: uppercase; white-space: nowrap;
  }
  .card--back .website { right: 18px; bottom: 14px; }
</style>
</head>
<body>
<main class="canvas">

  <section class="card card--front" aria-label="Business card front">
    <div class="ink-splash" role="img" aria-label="Grey ink splash with a music note"></div>
    <div class="brand-mark"><span class="dot"></span>Velvet Harbor Shows</div>
    <div class="person">
      <p class="person__name">Your full name here</p>
      <p class="person__title">Your title here</p>
    </div>
    <ul class="contact">
      <li><svg viewBox="0 0 10 10"><path d="M5 0a3.5 3.5 0 0 0-3.5 3.5C1.5 6 5 10 5 10s3.5-4 3.5-6.5A3.5 3.5 0 0 0 5 0zm0 5a1.5 1.5 0 1 1 0-3 1.5 1.5 0 0 1 0 3z"/></svg>Address line one, Address line 2, city, state 2345</li>
      <li><svg viewBox="0 0 10 10"><path d="M2 0l2 2.5-1 1.2a6 6 0 0 0 3.3 3.3l1.2-1L10 8l-1.5 2C4 10 0 6 0 1.5z"/></svg>2335-4556-3457</li>
      <li><svg viewBox="0 0 10 10"><path d="M2.5 0h5v10h-5zM3.5 1v7h3V1z"/></svg>7434-3345-4567</li>
      <li><svg viewBox="0 0 10 10"><path d="M0 2h10v6H0zM.8 2.6L5 5.6l4.2-3z" fill-rule="evenodd"/></svg>yourmail@email.com</li>
    </ul>
    <p class="website">www.velvetharborshows.com</p>
  </section>

  <section class="card card--back" aria-label="Business card back">
    <svg class="equalizer" viewBox="0 0 220 320" role="img" aria-label="Sound equalizer bars">
      <g opacity="0.9">
        <rect x="4"   y="40"  width="8" height="280"/>
        <rect x="16"  y="70"  width="8" height="250"/>
        <rect x="28"  y="30"  width="8" height="290"/>
        <rect x="40"  y="90"  width="8" height="230"/>
        <rect x="52"  y="60"  width="8" height="260"/>
        <rect x="64"  y="120" width="8" height="200"/>
        <rect x="76"  y="80"  width="8" height="240"/>
      </g>
      <g opacity="0.6">
        <rect x="88"  y="140" width="8" height="180"/>
        <rect x="100" y="110" width="8" height="210"/>
        <rect x="112" y="170" width="8" height="150"/>
        <rect x="124" y="150" width="8" height="170"/>
      </g>
      <g opacity="0.35">
        <rect x="136" y="200" width="8" height="120"/>
        <rect x="148" y="230" width="8" height="90"/>
        <rect x="160" y="210" width="8" height="110"/>
        <rect x="172" y="260" width="8" height="60"/>
      </g>
    </svg>
    <div class="tagline-block">
      <h1 class="tagline-block__name">Velvet Harbor Shows</h1>
      <p class="tagline-block__line">Produce alternative rock concerts</p>
    </div>
    <p class="website">www.velvetharborshows.com</p>
  </section>

</main>
</body>
</html>
```